Managed Service Provider need new business cards

We are a small Maanged Service Provider of IT Services and need a new fresh design for our business cards. We want something impossible, fun and professional :)
Our services has a large range, but we are always fun and make sure our customers both get their issue sorted and also feel like they are "catching up with an old friend".
All our cards in the past has always been all black, with red and we need something fresher.
The back of card, we would like just a small list of what we do i think, but if someone has a better idea, please do something cool with the back of the card:
Managed IT Services
Productivity Solutions
Data Backup and Recovery
IT System Maintenance
Managed IT Security
More details can be found on our website tqnetworks.com.au
Industry/Entity Type
It Company
Contact Information for Business Card
Name: Dwayne Falstrup
Title: Director
Phone: 03 6193 4827
Mobile: 0412 587 239
Email: dwayne@tqnetworks.com.au
Web: www.tqnetworks.com.au

```html
<!DOCTYPE html>
<html lang="en">
<head>
<meta charset="utf-8">
<title>TQ Networks business cards</title>
<link rel="stylesheet" href="https://fonts.googleapis.com/css2?family=Red+Hat+Text:wght@400;700&display=swap">
<style>
  :root {
    --bg: #e4e4e4;
    --ink: #111111;
    --card-dark: #0b0b0b;
    --card-light: #f4f4f4;
    --brand-red: #e31e25;
    --text-light: #f2f2f2;
    --map-tone-a: #1c1c1c;
    --map-tone-b: #0f0f0f;
  }
  * { margin: 0; padding: 0; box-sizing: border-box; }
  html, body {
    width: 1200px; height: 960px; overflow: hidden;
    background: var(--bg);
    font-family: "Red Hat Text", Arial, sans-serif;
  }
  .stage { position: relative; width: 1200px; height: 960px; }
  .card {
    position: absolute; left: 332px; width: 555px; height: 339px;
    overflow: hidden;
    box-shadow: 3px 4px 6px rgba(0,0,0,0.35);
  }
  .card-front { top: 132px; background: var(--card-dark); }
  .card-back { top: 517px; background: var(--card-light); }

  .network-map {
    position: absolute; left: 10px; top: 30px; width: 540px; height: 250px;
    background: radial-gradient(ellipse at 50% 50%, var(--map-tone-a) 0%, var(--map-tone-b) 75%, var(--card-dark) 100%);
  }
  .wordmark {
    position: absolute;
    font-family: "Red Hat Text", Arial, sans-serif;
    font-weight: 700;
    color: var(--brand-red);
    letter-spacing: 0.5px;
    white-space: nowrap;
  }
  .card-front .wordmark { left: 0; right: 0; top: 124px; text-align: center; font-size: 44px; }
  .service-list {
    position: absolute; left: 0; right: 0; top: 277px;
    text-align: center; color: var(--text-light);
    font-size: 14.5px; line-height: 19px;
  }

  .back-shapes { position: absolute; inset: 0; }
  .card-back .wordmark { left: 286px; top: 56px; font-size: 26px; letter-spacing: 0; }
  .person { position: absolute; left: 43px; top: 143px; }
  .person-name { color: var(--brand-red); font-weight: 700; font-size: 18px; line-height: 22px; }
  .person-title { color: var(--ink); font-size: 14px; line-height: 18px; }
  .contact-list {
    position: absolute; left: 286px; top: 188px; list-style: none;
    color: var(--ink); font-size: 14.5px; line-height: 18.5px;
  }
  .contact-list li { display: flex; align-items: center; gap: 5px; }
  .contact-icon { width: 13px; height: 13px; flex: none; }
</style>
</head>
<body>
<main class="stage">

  <section class="card card-front" aria-label="Card front">
    <div class="network-map" role="img" aria-label="Dark world map overlaid with connected network icons"></div>
    <div class="wordmark">TQ NETWORKS</div>
    <p class="service-list">
      Managed IT Services • Productivity Solutions • Managed It Security<br>
      Data Backup And Recovery • IT System Maintenance
    </p>
  </section>

  <section class="card card-back" aria-label="Card back">
    <svg class="back-shapes" width="555" height="339" viewBox="0 0 555 339" aria-hidden="true">
      <rect width="555" height="339" fill="var(--card-dark)"/>
      <path d="M0,0 H555 V246 C520,298 450,318 380,320 C290,322 230,268 140,270 C80,272 40,288 0,312 Z" fill="var(--brand-red)"/>
      <path d="M555,246 C520,298 450,318 380,320 C290,322 230,268 140,270 C80,272 40,288 0,312" fill="none" stroke="var(--card-light)" stroke-width="1.5"/>
      <path d="M0,0 H463 C520,40 562,150 549,218 C532,268 460,296 380,301 C300,306 220,248 130,258 C80,264 40,278 0,296 Z" fill="var(--card-light)"/>
    </svg>

    <div class="wordmark">TQ NETWORKS</div>

    <div class="person">
      <p class="person-name">Dwayne Falstrup</p>
      <p class="person-title">Director</p>
    </div>

    <ul class="contact-list">
      <li>
        <svg class="contact-icon" viewBox="0 0 16 16" aria-hidden="true"><path d="M3.5 1 L6 4 L4.5 6 C5.5 8 8 10.5 10 11.5 L12 10 L15 12.5 L13 15 C7 14.5 1.5 9 1 3 Z" fill="var(--brand-red)"/></svg>
        03 6193 4827
      </li>
      <li>
        <svg class="contact-icon" viewBox="0 0 16 16" aria-hidden="true"><rect x="4" y="1" width="8" height="14" rx="1.5" fill="none" stroke="var(--brand-red)" stroke-width="1.6"/><circle cx="8" cy="12.5" r="0.9" fill="var(--brand-red)"/></svg>
        0412 587 239
      </li>
      <li>
        <svg class="contact-icon" viewBox="0 0 16 16" aria-hidden="true"><rect x="1" y="3.5" width="14" height="9" fill="none" stroke="var(--brand-red)" stroke-width="1.6"/><path d="M1 3.5 L8 9 L15 3.5" fill="none" stroke="var(--brand-red)" stroke-width="1.6"/></svg>
        dwayne@tqnetworks.com.au
      </li>
      <li>
        <svg class="contact-icon" viewBox="0 0 16 16" aria-hidden="true"><circle cx="8" cy="8" r="6.5" fill="none" stroke="var(--brand-red)" stroke-width="1.4"/><ellipse cx="8" cy="8" rx="2.8" ry="6.5" fill="none" stroke="var(--brand-red)" stroke-width="1.2"/><path d="M1.5 8 H14.5" stroke="var(--brand-red)" stroke-width="1.2"/></svg>
        www.tqnetworks.com.au
      </li>
    </ul>
  </section>

</main>
</body>
</html>
```